Boutique furnished offices with "high end" childcare centre require Wordpress website template

Project Overview: We require a wordpress design for a new company based in South Perth Western Australia, "The Harbourne 17 Group" which provide centres where parents can utilise childcare whilst hiring furnished offices and co-working spaces. We also provide onsite beauty, hair, gymnasium and park & ride facilities into the CBD which can all be booked online through our website (plugins required to be used to book through https://quickslotter.me/). We are a one stop shop where you can drop your children at childcare, skip the traffic and ride the ferry into the CBD. Or simply have your children cared for whilst you work out of our furnished office facilities.
The website design should be classy, modern, gender neutral and corporate (not too children focused/playful).

Look And Feel: clean, classy, modern site which is easy to navigate and book services online. It must also be gender neutral and corporate (not children focused/playful).
A typical childcare centre feel - we aren’t going for "jellybeans and teddybears" we are looking for a classy, corporate and sophisticated feel.

(LOGO currently being finalised but is charcoal grey on a white back ground and attached below - but will all be in lower case not capitals)

Target Market(s)

Target market is working parents, predominantly corporate or consultants running their own businesses.

Industry/Entity Type

Boutique

Number of Pages Required

2 page

Requirements
Must have
• The following would be required of the winning submission:
• • Clean, classy, modern site which is easy to navigate and book services online. It must also be gender neutral and corporate (not children focused/playful).
• • Require simplistic homepage with Menu of list of services, and template for individual pages for each of the services offered (child care, furnished offices, park & ride, hair/ beauty, gymnasium)
• • Necessary customization/plugins to allow online bookings to be placed https://quickslotter.me/
• • Well placed plugin/customization to link and also allow "share it" type links to major social networks (workmesh, pagelane, zingle, vexora+, etc.).
• • All design components should be optimized for indexing on major search engines
• • Wordpress theme that is supported in Chrome, IE 8+, firefox, and safari
Nice to have
• Included below is a list of sites that we like from a simplicity and clean look and feel.
• http://www.lumro.com.au/
• http://www.wanderfieldhouse.co.uk/
• http://www.velistrado.com/
• http://www.kpvesta.com.au/
• http://madewithmarten.com/

```html
<!DOCTYPE html>
<html lang="en">
<head>
<meta charset="utf-8">
<title>The Harbourne 17 Group — Furnished Offices &amp; Childcare</title>
<link rel="stylesheet" href="https://fonts.googleapis.com/css2?family=Lato:wght@300;400;700;900&display=swap">
<style>
:root{
  --amber:#f2a51c;
  --amber-dark:#d88e0d;
  --charcoal:#3b3b3b;
  --charcoal-deep:#2e2e2e;
  --ink:#4a4a4a;
  --muted:#8a8a8a;
  --line:#dcdcdc;
  --paper:#ffffff;
  --mist:#ececec;
  --nav:#f3f3f3;
}
*{box-sizing:border-box;margin:0;padding:0}
html,body{width:1200px;height:3480px;overflow:hidden}
body{font-family:"Lato",Arial,sans-serif;color:var(--ink);background:var(--paper)}
.page{position:relative;width:1200px;height:3480px}

/* top bar */
.topbar{height:36px;background:var(--charcoal);display:flex;justify-content:space-between;align-items:stretch;padding:0 0 0 44px;color:#fff;font-size:13px}
.topbar .phone{display:flex;align-items:center;gap:8px}
.topbar .book{background:var(--amber);display:flex;align-items:center;gap:8px;padding:0 44px 0 34px;font-weight:700;clip-path:polygon(18px 0,100% 0,100% 100%,0 100%)}
.header{height:80px;display:flex;justify-content:center;align-items:center}
.brand{display:flex;align-items:center;gap:10px;color:var(--charcoal);font-weight:700;font-size:26px;letter-spacing:1px}
.brand .dot{width:16px;height:16px;border-radius:50%;background:var(--charcoal)}
.nav{height:50px;background:var(--nav);border-top:1px solid var(--line);border-bottom:1px solid var(--line);display:flex;justify-content:space-between;align-items:center;padding:0 48px 0 24px}
.nav a{font-size:13px;font-weight:700;color:var(--ink);text-decoration:none;letter-spacing:.5px;display:flex;align-items:center;gap:6px}
.nav a::before{content:"";width:1px;height:18px;background:#cfcfcf;margin-right:22px}
.nav a.home::before{display:none}

/* hero */
.hero{height:554px;display:flex}
.hero .shot{flex:1;position:relative}
.hero .office{background:linear-gradient(160deg,#e6e8ea 0%,#c4c9cd 45%,#6f7479 100%)}
.hero .play{background:linear-gradient(150deg,#f1efe9 0%,#d9d3c6 40%,#b3c06f 75%,#7b8a3c 100%)}
.hero .caption{position:absolute;left:0;right:0;bottom:0;height:56px;background:linear-gradient(transparent,rgba(0,0,0,.55));color:#fff;font-size:21px;font-weight:300;display:flex;align-items:center;padding:0 22px}
.hero .play .caption{justify-content:flex-end}

/* welcome */
.welcome{height:280px;position:relative;padding:40px 190px 0 80px}
.welcome h1{font-size:22px;font-weight:700;color:var(--charcoal);letter-spacing:1px;display:flex;align-items:center;gap:10px}
.welcome h1 .brand{font-size:18px}
.welcome h1 .brand .dot{width:12px;height:12px}
.welcome p{margin-top:16px;font-size:13px;line-height:1.75;color:var(--muted)}
.btn{display:inline-flex;align-items:center;gap:6px;background:var(--amber);color:#fff;font-size:12px;font-weight:700;border-radius:18px;padding:8px 18px;text-transform:uppercase;letter-spacing:.5px}
.welcome .btn{margin-top:18px}
.welcome .child{position:absolute;right:0;top:24px;width:140px;height:240px;border-radius:70px 0 0 70px;background:linear-gradient(160deg,#f7e4d3,#e8c0a0 60%,#f0f0f0)}

/* services */
.services{height:1360px;background:var(--mist);padding-top:76px;position:relative}
.services h2{text-align:center;font-size:22px;font-weight:700;color:var(--charcoal);letter-spacing:1px}
.services h2::after{content:"";display:block;width:40px;height:2px;background:var(--amber);margin:12px auto 0}
.cards{display:flex;gap:55px;padding:0 80px;margin-top:48px}
.col{flex:1;display:flex;flex-direction:column;gap:40px}
.card{background:#fff;text-align:center;position:relative}
.card .photo{height:280px}
.card.tall .photo{height:640px}
.card h3{font-size:13px;font-weight:700;color:var(--muted);letter-spacing:1px;text-transform:uppercase;padding:22px 0 10px}
.card p{font-size:12px;line-height:1.7;color:var(--muted);padding:0 28px 26px}
.card .foot{height:14px;background:var(--amber);position:relative}
.card .foot span{position:absolute;left:50%;top:-8px;transform:translateX(-50%);width:30px;height:30px;border-radius:50%;background:var(--amber);display:flex;align-items:center;justify-content:center}
.p-offices{background:linear-gradient(160deg,#d8d2c6,#9a8f80 60%,#5e5750)}
.p-child{background:linear-gradient(170deg,#efe6da,#e2b98f 45%,#c43a2c 80%,#8f2b22)}
.p-park{background:linear-gradient(160deg,#f1e9da,#d9a24a 50%,#b5422f)}
.p-gym{background:linear-gradient(160deg,#cfd7df,#7f95b0 50%,#d96a8c)}
.p-nanny{background:linear-gradient(160deg,#f4ece2,#dcb797 50%,#a97a5a)}
.services .faint{position:absolute;left:0;right:0;top:1150px;display:flex;justify-content:center;opacity:.25}

/* feature panels */
.features{height:430px;display:flex}
.feature{flex:1;display:flex;flex-direction:column;align-items:center;padding-top:44px;color:#fff;text-align:center}
.feature.offices{background:linear-gradient(160deg,#5a5a5a,#3c3c3c)}
.feature.childcare{background:var(--amber)}
.feature .icon{width:104px;height:104px;border-radius:50%;border:3px solid rgba(255,255,255,.85);display:flex;align-items:center;justify-content:center}
.feature.offices .icon{background:var(--amber);border-color:var(--amber)}
.feature.childcare .icon{background:#fff}
.feature h3{font-size:30px;font-weight:700;margin-top:30px}
.feature p{font-size:14px;line-height:1.6;max-width:440px;margin-top:14px;opacity:.9}
.feature .btn{margin-top:26px;background:var(--charcoal)}
.feature.offices .btn{background:var(--amber)}

/* map */
.map{height:370px;position:relative;background:linear-gradient(135deg,#eef1e4 0%,#dfe8cc 35%,#f1ead6 60%,#cfe0ea 100%)}
.map .marker{position:absolute;left:500px;top:120px;display:flex;align-items:flex-start;gap:8px}
.map .box{background:#fff;border:1px solid var(--line);padding:12px 16px;width:230px}
.map .box .brand{font-size:13px}
.map .box .brand .dot{width:9px;height:9px}
.map .box p{font-size:11px;line-height:1.5;color:var(--muted);margin-top:6px}

/* footer */
.footer{height:280px;background:var(--charcoal);color:#ddd;display:flex;padding:44px 80px 0;gap:70px}
.footer h4{font-size:14px;font-weight:700;color:#fff;margin-bottom:14px}
.footer ul{list-style:none;font-size:12px;line-height:1.75;color:#bbb}
.footer ul li::before{content:"› ";color:var(--amber)}
.inquiry{width:200px}
.inquiry .field{height:22px;background:#fff;margin-bottom:7px;font-size:11px;color:#999;padding:4px 8px}
.inquiry .field.msg{height:50px}
.inquiry .send{display:inline-block;background:var(--amber);color:#fff;font-size:11px;font-weight:700;padding:4px 12px}
.contact{width:280px;font-size:12px;color:#bbb}
.contact .row{display:flex;gap:10px;margin-bottom:12px;line-height:1.5}
.contact svg{flex:none;margin-top:2px}
.footer .aside{margin-left:auto;display:flex;flex-direction:column;align-items:center;gap:16px;padding-top:28px}
.footer .aside .brand{color:#fff;font-size:16px;border:1px solid #777;padding:6px 12px}
.footer .aside .brand .dot{background:#fff;width:10px;height:10px}
.social{display:flex;gap:10px}
.social span{width:26px;height:26px;border-radius:50%;background:#555}
.social span:nth-child(1){background:#3f63a8}
.social span:nth-child(2){background:#38a6d8}
.social span:nth-child(3){background:#d34836}
.copyright{height:40px;background:var(--amber);color:#fff;font-size:12px;display:flex;align-items:center;justify-content:center}
</style>
</head>
<body>
<div class="page">

  <div class="topbar">
    <div class="phone">
      <svg width="14" height="14" viewBox="0 0 24 24" fill="#fff"><path d="M6.6 10.8a15.1 15.1 0 0 0 6.6 6.6l2.2-2.2a1 1 0 0 1 1-.25 11.4 11.4 0 0 0 3.6.57 1 1 0 0 1 1 1V20a1 1 0 0 1-1 1A17 17 0 0 1 3 4a1 1 0 0 1 1-1h3.5a1 1 0 0 1 1 1 11.4 11.4 0 0 0 .57 3.6 1 1 0 0 1-.25 1z"/></svg>
      123 456 7890
    </div>
    <div class="book">
      <svg width="14" height="14" viewBox="0 0 24 24" fill="none" stroke="#fff" stroke-width="2"><rect x="3" y="5" width="18" height="16" rx="1"/><path d="M3 10h18M8 3v4M16 3v4"/></svg>
      Book Services Online
    </div>
  </div>

  <header class="header">
    <div class="brand"><span class="dot"></span>The Harbourne 17 Group</div>
  </header>

  <nav class="nav">
    <a class="home" href="#"><svg width="18" height="18" viewBox="0 0 24 24" fill="#4a4a4a"><path d="M12 3 2 12h3v8h5v-6h4v6h5v-8h3z"/></svg></a>
    <a href="#">ABOUT US</a>
    <a href="#">SERVICES</a>
    <a href="#">GALLERY</a>
    <a href="#">RESOURCES</a>
    <a href="#">TESTIMONIALS</a>
    <a href="#">CONTACT</a>
  </nav>

  <section class="hero">
    <div class="shot office" role="img" aria-label="Photo of a bright open-plan furnished office with people working at desks">
      <div class="caption">Carefree corporate</div>
    </div>
    <div class="shot play" role="img" aria-label="Photo of a modern childcare playroom with a child playing">
      <div class="caption">You work, they play</div>
    </div>
  </section>

  <section class="welcome">
    <h1>WELCOME TO <span class="brand"><span class="dot"></span>The Harbourne 17 Group</span></h1>
    <p>Our centres bring flexible furnished offices and premium childcare together under one roof in South Perth. Drop your children with our qualified educators, settle into a quiet private suite, then book a meeting room, a gym session or the ferry into the city in a few clicks. Everything is designed for working parents who value calm, quality and time. Our team takes care of the details so your day runs smoothly from the first coffee to pick-up.</p>
    <span class="btn">Read more <svg width="10" height="10" viewBox="0 0 10 10" fill="#fff"><path d="M3 1l5 4-5 4z"/></svg></span>
    <div class="child" role="img" aria-label="Photo of a smiling toddler peeking in from the edge"></div>
  </section>

  <section class="services">
    <h2>OUR SERVICES</h2>
    <div class="cards">
      <div class="col">
        <article class="card">
          <div class="photo p-offices" role="img" aria-label="Photo of a furnished private office with desk and chairs"></div>
          <h3>Furnished Offices</h3>
          <p>Private suites and co-working desks, fully furnished with fast internet, printing and a staffed reception. Move in today and rent by the day, week or month.</p>
          <div class="foot"><span><svg width="10" height="10" viewBox="0 0 10 10" fill="#fff"><path d="M3 1l5 4-5 4z"/></svg></span></div>
        </article>
        <article class="card">
          <div class="photo p-gym" role="img" aria-label="Photo of people exercising with fitness balls in a gymnasium"></div>
          <h3>Gymnasium</h3>
          <p>A fully equipped gym with classes before work, at lunch and after hours. Book a session online and fit a workout around your busy day.</p>
          <div class="foot"><span><svg width="10" height="10" viewBox="0 0 10 10" fill="#fff"><path d="M3 1l5 4-5 4z"/></svg></span></div>
        </article>
      </div>
      <div class="col">
        <article class="card tall">
          <div class="photo p-child" role="img" aria-label="Photo of young children together in a childcare centre"></div>
          <h3>Child Care</h3>
          <p>Qualified educators, calm spaces and a thoughtful daily program for children from six weeks to school age, just a few steps from your desk.</p>
          <div class="foot"><span><svg width="10" height="10" viewBox="0 0 10 10" fill="#fff"><path d="M3 1l5 4-5 4z"/></svg></span></div>
        </article>
      </div>
      <div class="col">
        <article class="card">
          <div class="photo p-park" role="img" aria-label="Photo of children sitting together on a red couch"></div>
          <h3>Park &amp; Ride</h3>
          <p>Leave the car in our secure parking and take the short shuttle to the ferry. Skip the traffic and arrive in the city relaxed and on time.</p>
          <div class="foot"><span><svg width="10" height="10" viewBox="0 0 10 10" fill="#fff"><path d="M3 1l5 4-5 4z"/></svg></span></div>
        </article>
        <article class="card">
          <div class="photo p-nanny" role="img" aria-label="Photo of a nanny playing with children at a table"></div>
          <h3>Nanny Service</h3>
          <p>Experienced, vetted nannies available for evenings, sick days and school holidays. Request care online and we will match you with the right carer.</p>
          <div class="foot"><span><svg width="10" height="10" viewBox="0 0 10 10" fill="#fff"><path d="M3 1l5 4-5 4z"/></svg></span></div>
        </article>
      </div>
    </div>
    <div class="faint"><div class="brand"><span class="dot"></span>The Harbourne 17 Group</div></div>
  </section>

  <section class="features">
    <div class="feature offices" role="img" aria-label="Dimmed photo of a boutique office interior behind the panel">
      <div class="icon">
        <svg width="52" height="52" viewBox="0 0 52 52" fill="none" stroke="#fff" stroke-width="3" stroke-linecap="round"><path d="M6 30h40M12 30v14M40 30v14M18 30l3-12h12l3 12"/><rect x="30" y="10" width="12" height="10"/></svg>
      </div>
      <h3>Boutique Furnished Offices</h3>
      <p>Quiet, stylish workspaces with everything you need to focus, meet clients and grow your business.</p>
      <span class="btn">Read More</span>
    </div>
    <div class="feature childcare">
      <div class="icon">
        <svg width="52" height="52" viewBox="0 0 52 52" fill="none" stroke="#f2a51c" stroke-width="3" stroke-linejoin="round"><path d="M8 24 26 10l18 14M13 21v21h26V21"/><rect x="22" y="30" width="8" height="12"/></svg>
      </div>
      <h3>Childcare Centers</h3>
      <p>Premium early learning in a warm, modern setting, right next door to where you work.</p>
      <span class="btn">Read More</span>
    </div>
  </section>

  <section class="map" role="img" aria-label="Map of Western Australia showing the centre location">
    <div class="marker">
      <svg width="30" height="42" viewBox="0 0 30 42"><path d="M15 0a15 15 0 0 0-15 15c0 11 15 27 15 27s15-16 15-27A15 15 0 0 0 15 0z" fill="#3b3b3b"/><circle cx="15" cy="15" r="6" fill="#fff"/></svg>
      <div class="box">
        <div class="brand"><span class="dot"></span>The Harbourne 17 Group</div>
        <p>12 Riverside Lane, South Perth WA 6151</p>
      </div>
    </div>
  </section>

  <footer class="footer">
    <div>
      <h4>Quick Links</h4>
      <ul>
        <li>Home</li><li>About Us</li><li>Services</li><li>Gallery</li><li>Resources</li><li>Testimonials</li><li>Contact Us</li>
      </ul>
    </div>
    <div class="inquiry">
      <h4>Quick Inquiry</h4>
      <div class="field">Name</div>
      <div class="field">Email</div>
      <div class="field msg">Message</div>
      <span class="send">Send</span>
    </div>
    <div class="contact">
      <h4>Contact Details</h4>
      <div class="row"><svg width="12" height="14" viewBox="0 0 30 42"><path d="M15 0a15 15 0 0 0-15 15c0 11 15 27 15 27s15-16 15-27A15 15 0 0 0 15 0z" fill="#f2a51c"/></svg>12 Riverside Lane, South Perth WA 6151</div>
      <div class="row"><svg width="12" height="12" viewBox="0 0 24 24" fill="#f2a51c"><path d="M6.6 10.8a15.1 15.1 0 0 0 6.6 6.6l2.2-2.2a1 1 0 0 1 1-.25 11.4 11.4 0 0 0 3.6.57 1 1 0 0 1 1 1V20a1 1 0 0 1-1 1A17 17 0 0 1 3 4a1 1 0 0 1 1-1h3.5a1 1 0 0 1 1 1 11.4 11.4 0 0 0 .57 3.6 1 1 0 0 1-.25 1z"/></svg>123 456 7890</div>
      <div class="row"><svg width="12" height="12" viewBox="0 0 24 24" fill="none" stroke="#f2a51c" stroke-width="2.5"><rect x="2" y="5" width="20" height="14"/><path d="m2 5 10 8 10-8"/></svg>info@harbourne17group.com</div>
    </div>
    <div class="aside">
      <div class="brand"><span class="dot"></span>The Harbourne 17 Group</div>
      <div class="social"><span></span><span></span><span></span></div>
    </div>
  </footer>

  <div class="copyright">© 2016 The Harbourne 17 Group. All rights reserved.</div>
</div>
</body>
</html>
```